Emergency Management Consulting Flyer

Company name: Stone Harbor Emergency Management

I am looking for a postcard design for my emergency management consulting business. I'm looking for something that has some colors and is double sided, on side with the information on services provided and the other side with the contact information. For the main side I'm looking for the following:

How prepared are you?

Services Provided:
Healthcare Preparedness
EOC Support
Emergency Planning
Mitigation Planning
Business Continuity
Disaster Response
Training and Exercises
Project Management
And more

Affordable for small and large organizations
Stand-by contracts available

On the back side, I'm looking for Contact Us section.

Overall I'm looking for something a bit more modern and need to have at least one disaster photo. If you have questions please message me.

Target Market(s)

Government, Healthcare Facilities, Businesses

Industry/Entity Type

Consulting

Requirements
Must have
• Disaster Picture, modern looking
• For the main side I'm looking for the following:
• How prepared are you?
• Services Provided:
• Healthcare Preparedness
• EOC Support
• Emergency Planning
• Mitigation Planning
• Business Continuity
• Disaster Response
• Training and Exercises
• Project Management
• And more
• Affordable for small and large organizations
• Stand-by contracts available

```html
<!DOCTYPE html>
<html lang="en">
<head>
<meta charset="utf-8">
<title>Stone Harbor Emergency Management – Postcard</title>
<link href="https://fonts.googleapis.com/css2?family=Krona+One&family=Arimo:wght@400;700&display=swap" rel="stylesheet">
<style>
  :root{
    --bg:#d9d3c7;
    --paper:#ffffff;
    --red:#e5392b;
    --orange-red:#e8452c;
    --band-blue:#1f9bd7;
    --deep-blue:#1b6db6;
    --yellow:#fbc65a;
    --black:#222222;
    --ink:#333333;
    --rule:#555555;
  }
  *{box-sizing:border-box;margin:0;padding:0}
  html,body{width:900px;height:1200px;overflow:hidden}
  body{background:var(--bg);position:relative;font-family:"Arimo",Arial,sans-serif;color:var(--ink)}
  .card{position:absolute;left:147px;width:594px;height:414px;background:var(--paper);overflow:hidden}
  .card--front{top:192px}
  .card--back{top:644px;height:412px}
  .card-art{position:absolute;inset:0}
  .brand{position:absolute;display:flex;align-items:center;gap:8px;
    font-family:"Arimo",Arial,sans-serif;font-weight:700;color:var(--ink);line-height:1.05;font-size:13px;letter-spacing:.4px}
  .brand-dot{width:22px;height:22px;border-radius:50%;background:var(--orange-red);flex:none}
  .brand-name span{display:block;white-space:nowrap}
  .front-brand{left:25px;top:28px}
  .headline{position:absolute;left:24px;top:80px;font-family:"Krona One",sans-serif;font-size:20px;line-height:27px;color:var(--orange-red);font-weight:400;white-space:nowrap}
  .services-band{position:absolute;left:0;top:145px;width:228px;height:21px;background:var(--band-blue);color:#fff;font-weight:700;font-size:13px;padding:3px 0 0 24px;letter-spacing:.3px}
  .services-list{position:absolute;left:24px;top:174px;list-style:none;font-size:12.5px;line-height:18px;color:var(--ink)}
  .services-list li::before{content:"➢";color:var(--red);font-size:9px;margin-right:5px;vertical-align:1px}
  .offer{position:absolute;left:24px;top:328px;font-family:"Krona One",sans-serif;font-size:9.6px;line-height:17.5px;color:var(--red);white-space:nowrap}
  .web-band{position:absolute;left:0;bottom:0;width:240px;height:27px;background:var(--deep-blue);color:#fff;font-family:"Krona One",sans-serif;font-size:9.5px;padding:8px 0 0 24px;white-space:nowrap}
  .back-brand{left:28px;top:40px}
  .back-brand .brand-name{color:#fff}
  .blurb{position:absolute;left:26px;top:86px;width:200px;font-weight:700;font-size:12.5px;line-height:14px;color:var(--red);text-align:justify}
  .contact-band{position:absolute;left:0;top:292px;width:228px;height:38px;background:var(--deep-blue);color:#fff;font-size:10.5px;
    display:grid;grid-template-columns:134px 86px;row-gap:3px;padding:5px 0 0 8px}
  .contact-item{display:flex;align-items:center;gap:5px;white-space:nowrap}
  .contact-item svg{width:9px;height:9px;flex:none}
  .stamp-box{position:absolute;left:474px;top:30px;width:92px;height:81px;border:1px solid var(--rule)}
  .address-line{position:absolute;left:384px;width:182px;height:1px;background:var(--rule)}
</style>
</head>
<body>

<section class="card card--front">
  <svg class="card-art" viewBox="0 0 594 414" width="594" height="414">
    <defs>
      <linearGradient id="floodPhoto" x1="0" y1="0" x2="0" y2="1">
        <stop offset="0" stop-color="#e6ecef"/>
        <stop offset=".45" stop-color="#b9a99a"/>
        <stop offset=".7" stop-color="#8c7a66"/>
        <stop offset="1" stop-color="#7a6a58"/>
      </linearGradient>
    </defs>
    <polygon role="img" aria-label="Photo of a flooded house with collapsed roofing" fill="url(#floodPhoto)" points="300,0 594,0 594,414 250,414"/>
    <polygon fill="var(--red)" points="245,0 290,0 328,110 300,150"/>
    <polygon fill="var(--yellow)" points="285,0 450,0 335,125"/>
    <polygon fill="var(--band-blue)" opacity=".85" points="335,55 385,95 300,414 255,414"/>
    <polygon fill="var(--deep-blue)" opacity=".9" points="340,55 360,52 285,414 262,414"/>
    <polygon fill="var(--yellow)" points="235,414 282,330 300,414"/>
    <polygon fill="var(--red)" points="268,414 298,320 330,414"/>
  </svg>

  <div class="brand front-brand">
    <span class="brand-dot"></span>
    <span class="brand-name"><span>STONE HARBOR</span><span>EMERGENCY MANAGEMENT</span></span>
  </div>
  <h1 class="headline">How prepared<br>are you?</h1>
  <div class="services-band">SERVICES PROVIDED:</div>
  <ul class="services-list">
    <li>Healthcare Preparedness</li>
    <li>EOC Support</li>
    <li>Emergency Planning</li>
    <li>Mitigation Planning</li>
    <li>Business Continuity</li>
    <li>Disaster Response</li>
    <li>Training and Exercises</li>
    <li>Project Management</li>
  </ul>
  <p class="offer">Affordable for small and large<br>organizations Stand-by<br>contracts available</p>
  <div class="web-band">www.stoneharborem.com</div>
</section>

<section class="card card--back">
  <svg class="card-art" viewBox="0 0 594 412" width="594" height="412">
    <defs>
      <linearGradient id="debrisPhoto" x1="0" y1="0" x2="0" y2="1">
        <stop offset="0" stop-color="#d9dde0"/>
        <stop offset=".35" stop-color="#9aa5ad"/>
        <stop offset=".7" stop-color="#4f6072"/>
        <stop offset="1" stop-color="#34465a"/>
      </linearGradient>
    </defs>
    <polygon role="img" aria-label="Photo of a disaster zone covered in debris and wrecked cars" fill="url(#debrisPhoto)" points="0,0 290,0 215,330 0,330"/>
    <polygon fill="var(--black)" points="245,0 300,0 270,130"/>
    <polygon fill="var(--yellow)" points="290,0 390,0 285,120"/>
    <polygon fill="var(--yellow)" opacity=".7" points="285,40 350,60 250,250"/>
    <polygon fill="var(--deep-blue)" opacity=".9" points="300,55 320,70 238,330 228,330"/>
    <polygon fill="var(--band-blue)" opacity=".7" points="275,90 310,70 240,310"/>
    <polygon fill="var(--yellow)" points="228,330 248,250 252,330"/>
    <polygon fill="var(--red)" points="218,330 236,290 242,330"/>
  </svg>

  <div class="brand back-brand">
    <span class="brand-dot"></span>
    <span class="brand-name"><span>STONE HARBOR</span><span>EMERGENCY MANAGEMENT</span></span>
  </div>
  <p class="blurb">Lorem ipsum dolor sit amet, consectetur adipiscing elit. Donec nec erat ut mi maximus maximus vel at arcu.</p>

  <div class="contact-band">
    <span class="contact-item"><svg viewBox="0 0 10 10"><path fill="#fff" d="M5 0a3.5 3.5 0 0 0-3.5 3.5C1.5 6 5 10 5 10s3.5-4 3.5-6.5A3.5 3.5 0 0 0 5 0zm0 5a1.5 1.5 0 1 1 0-3 1.5 1.5 0 0 1 0 3z"/></svg>stoneharbor.24061</span>
    <span class="contact-item"><svg viewBox="0 0 10 10"><circle cx="5" cy="5" r="5" fill="#fff"/><path fill="#1b6db6" d="M3 2.5l1 .2.4 1.2-.6.5a4 4 0 0 0 1.8 1.8l.5-.6 1.2.4.2 1-.8.6C4.8 7.4 2.6 5.2 2.4 3.3z"/></svg>5550142087</span>
    <span class="contact-item"><svg viewBox="0 0 10 10"><circle cx="5" cy="5" r="4.3" fill="none" stroke="#fff"/><path d="M.7 5h8.6M5 .7c-2 2.5-2 6.1 0 8.6M5 .7c2 2.5 2 6.1 0 8.6" stroke="#fff" fill="none" stroke-width=".7"/></svg>www.stoneharborem.com</span>
    <span class="contact-item"><svg viewBox="0 0 10 10"><circle cx="5" cy="5" r="5" fill="#fff"/><rect x="3.3" y="2" width="3.4" height="6" rx=".6" fill="#1b6db6"/></svg>5550142087</span>
  </div>

  <div class="stamp-box"></div>
  <div class="address-line" style="top:157px"></div>
  <div class="address-line" style="top:191px"></div>
  <div class="address-line" style="top:225px"></div>
  <div class="address-line" style="top:259px"></div>
</section>

</body>
</html>
```